Fitness competition business needs a card design

I need a professional business card design using my logo. The card will be horizontal with rounded edges.

Target Market(s)

Female fitness competitors

Industry/Entity Type

Fitness

Contact Information for Business Card

Rose-Lynn Darby
Owner
stagevarno.com
555.301.2187
info@stagevarno.com

Font styles to use
Serif

Colors

Designer to choose colors to be used in the design.

Requirements
Must have
• On the back please add the following:
• Figure
• Bikini
• Physique
• Fitness
Nice to have
• Looking for a very sleek design, contemporary and easy to read.
Should not have
• Should not be difficult to read or be too busy

```html
<!DOCTYPE html>
<html lang="en">
<head>
<meta charset="utf-8">
<title>Stage Varno – Business Card</title>
<link rel="stylesheet" href="https://fonts.googleapis.com/css2?family=Montserrat:wght@400;500;600;800&display=swap">
<style>
  :root {
    --stage-bg: #b9b9b9;
    --card-black: #161616;
    --card-white: #f3f3f1;
    --brand-red: #e01e26;
    --ink-dark: #3a3a3a;
    --ink-mid: #555555;
    --ink-light: #f2f2f2;
    --divider: #c9c9c9;
  }
  * { box-sizing: border-box; margin: 0; padding: 0; }
  html, body { width: 1200px; height: 1000px; overflow: hidden; }
  body {
    background: radial-gradient(circle at 50% 40%, #dcdcdc 0%, var(--stage-bg) 75%);
    font-family: "Montserrat", Arial, sans-serif;
    position: relative;
  }
  .card {
    position: absolute;
    width: 660px;
    height: 377px;
    border-radius: 34px;
    box-shadow: 0 12px 30px rgba(0,0,0,.25);
  }
  .card--front {
    left: 90px; top: 90px;
    background: linear-gradient(160deg, #262626 0%, var(--card-black) 60%, #0d0d0d 100%);
    display: flex; flex-direction: column; align-items: center; justify-content: center;
  }
  .card--back {
    left: 450px; top: 523px;
    background: var(--card-white);
    display: flex; align-items: center;
  }
  .brand {
    display: flex; align-items: center; gap: 14px;
  }
  .brand__mark {
    width: 22px; height: 22px; background: var(--brand-red);
  }
  .brand__name {
    font-weight: 800; color: var(--brand-red);
    font-size: 46px; letter-spacing: 1px; text-transform: uppercase;
  }
  .categories {
    margin-top: 34px;
    color: var(--ink-light);
    font-size: 15px; font-weight: 500; letter-spacing: 1.5px;
    text-transform: uppercase;
    display: flex; gap: 10px; align-items: center;
  }
  .categories__sep { color: var(--brand-red); font-weight: 600; }
  .card--back .brand-area {
    width: 370px; display: flex; justify-content: center;
  }
  .card--back .brand__name { font-size: 38px; }
  .card--back .brand__mark { width: 18px; height: 18px; }
  .divider {
    width: 1px; height: 200px; background: var(--divider);
  }
  .contact { padding-left: 26px; }
  .contact__name {
    color: var(--brand-red); font-weight: 600; font-size: 19px;
  }
  .contact__role {
    color: var(--ink-dark); font-size: 13px; margin: 2px 0 16px 8px;
  }
  .contact__list { list-style: none; }
  .contact__item {
    display: flex; align-items: center; gap: 8px;
    color: var(--ink-mid); font-size: 15px; margin-bottom: 6px;
  }
  .contact__icon { width: 13px; height: 13px; flex: none; }
</style>
</head>
<body>
  <section class="card card--front" aria-label="Card front">
    <div class="brand">
      <span class="brand__mark"></span>
      <span class="brand__name">Stage Varno</span>
    </div>
    <p class="categories">
      <span>Figure</span><span class="categories__sep">|</span>
      <span>Bikini</span><span class="categories__sep">|</span>
      <span>Physique</span><span class="categories__sep">|</span>
      <span>Fitness</span>
    </p>
  </section>

  <section class="card card--back" aria-label="Card back">
    <div class="brand-area">
      <div class="brand">
        <span class="brand__mark"></span>
        <span class="brand__name">Stage Varno</span>
      </div>
    </div>
    <div class="divider"></div>
    <div class="contact">
      <p class="contact__name">Rose-Lynn Darby</p>
      <p class="contact__role">Owner</p>
      <ul class="contact__list">
        <li class="contact__item">
          <svg class="contact__icon" viewBox="0 0 14 14" aria-hidden="true"><circle cx="7" cy="7" r="6" fill="none" stroke="#e01e26" stroke-width="1.5"/><ellipse cx="7" cy="7" rx="2.5" ry="6" fill="none" stroke="#e01e26" stroke-width="1.2"/><line x1="1" y1="7" x2="13" y2="7" stroke="#e01e26" stroke-width="1.2"/></svg>
          stagevarno.com
        </li>
        <li class="contact__item">
          <svg class="contact__icon" viewBox="0 0 14 14" aria-hidden="true"><path d="M3 1.5l2.2 2.6-1.2 1.6c.9 1.8 2.3 3.2 4.1 4.1l1.6-1.2 2.6 2.2-1.3 1.7C6 12.2 1.8 8 1.3 2.8z" fill="#e01e26"/></svg>
          555.301.2187
        </li>
        <li class="contact__item">
          <svg class="contact__icon" viewBox="0 0 14 14" aria-hidden="true"><rect x="1" y="3" width="12" height="9" rx="1" fill="#e01e26"/><path d="M1.5 3.5L7 8l5.5-4.5" fill="none" stroke="#fff" stroke-width="1.2"/></svg>
          info@stagevarno.com
        </li>
      </ul>
    </div>
  </section>
</body>
</html>
```